Business Card Design for Concierge business

Hi. I would like to have an elegant, smart business card for my concierge business, called Harbor Concierge. The services I provide are mail management, dog walking, cleaning, car, stylist, personal shopper, running errands, property management, event planning. I was thinking to add my picture but I would like to see options without it as well, if possible.

Thank you.

Business Card Details:
*Designers are to solely use contact information for the business card design. This is not to be used to contact the customer*

Name: Tamsin Heller
mail: quaylineerrands@mailvora.net
Phone: 305-482-9167

Target Market(s)

vacation home owners

Industry/Entity Type

Business

Font styles to use
Serif

Colors

Designer to choose colors to be used in the design.

Requirements
Nice to have
• Could use icons that describe the services I provide for example car, house, key, shopping cart, shopping bags, envelope, champagne glasses, phone, dog etc.

```html
<!DOCTYPE html>
<html lang="en">
<head>
<meta charset="utf-8">
<title>Harbor Concierge – Business Cards</title>
<link rel="stylesheet" href="https://fonts.googleapis.com/css2?family=Cinzel:wght@400;600&family=Cormorant+Garamond:wght@500;600&display=swap">
<style>
  :root {
    --teal: #3fbf98;
    --ink: #0b0b0b;
    --ink-soft: #1d1d1d;
    --paper: #ffffff;
    --stage: #ece9e4;
    --light-text: #f2f2f2;
    --dark-text: #111111;
  }
  * { margin: 0; padding: 0; box-sizing: border-box; }
  html, body { width: 1200px; height: 784px; overflow: hidden; }
  body { background: var(--stage); position: relative; font-family: "Cormorant Garamond", Georgia, serif; }

  .card {
    position: absolute;
    width: 560px;
    height: 320px;
    border-radius: 4px;
    overflow: hidden;
    box-shadow: 0 10px 24px rgba(0,0,0,.25);
  }

  /* Back: services */
  .card--services {
    left: 60px; top: 70px;
    background: radial-gradient(ellipse at 55% 45%, #262626 0%, var(--ink-soft) 35%, var(--ink) 80%);
    color: var(--light-text);
  }
  .brand {
    font-family: "Cinzel", Georgia, serif;
    font-weight: 600;
    letter-spacing: 2px;
    text-align: center;
  }
  .card--services .brand {
    position: absolute; top: 38px; left: 0; right: 0;
    font-size: 20px; color: var(--light-text);
  }
  .services { position: absolute; top: 92px; list-style: none; }
  .services--left { left: 44px; }
  .services--right { left: 318px; }
  .services li {
    display: flex; align-items: center; gap: 14px;
    height: 38px;
    font-family: "Cinzel", Georgia, serif;
    font-size: 12px; letter-spacing: 1px; text-transform: uppercase;
  }
  .services svg { width: 30px; height: 26px; flex: none; fill: var(--teal); }

  /* Front: contact */
  .card--contact { left: 580px; top: 390px; background: var(--paper); }
  .card--contact > svg.backdrop { position: absolute; inset: 0; }
  .card--contact .brand {
    position: absolute; top: 92px; left: 250px; width: 260px;
    font-size: 22px; color: var(--dark-text);
  }
  .portrait {
    position: absolute; left: 100px; top: 88px; width: 150px; height: 232px;
    border-radius: 70px 70px 0 0;
    background: linear-gradient(180deg, #4a3a33 0%, #8a7d74 45%, #c9c4be 100%);
  }
  .contact { position: absolute; left: 330px; top: 196px; color: var(--light-text); }
  .contact__name { color: var(--teal); font-size: 22px; font-weight: 600; margin-bottom: 10px; }
  .contact__line { display: flex; align-items: center; gap: 10px; font-size: 16px; height: 24px; }
  .contact__line svg { width: 14px; height: 14px; fill: var(--teal); flex: none; }
</style>
</head>
<body>

<section class="card card--services" aria-label="Back of card: services">
  <div class="brand">Harbor Concierge</div>
  <ul class="services services--left">
    <li><svg viewBox="0 0 30 26" aria-hidden="true"><path d="M2 4h26v18H2z"/><path d="M2 4l13 10 13-10" fill="none" stroke="#0b0b0b" stroke-width="2"/></svg>Mail Management</li>
    <li><svg viewBox="0 0 30 26" role="img" aria-label="dog walking icon"><rect x="4" y="3" width="22" height="20" rx="5"/></svg>Dog Walking</li>
    <li><svg viewBox="0 0 30 26" role="img" aria-label="cleaning icon"><rect x="4" y="3" width="22" height="20" rx="5"/></svg>Cleaning</li>
    <li><svg viewBox="0 0 30 26" aria-hidden="true"><path d="M2 14l4-6h16l5 6v6H2z"/><circle cx="8" cy="21" r="3" stroke="#0b0b0b" stroke-width="1.5"/><circle cx="22" cy="21" r="3" stroke="#0b0b0b" stroke-width="1.5"/></svg>Car</li>
    <li><svg viewBox="0 0 30 26" role="img" aria-label="stylist icon"><rect x="4" y="3" width="22" height="20" rx="5"/></svg>Stylist</li>
  </ul>
  <ul class="services services--right">
    <li><svg viewBox="0 0 30 26" aria-hidden="true"><path d="M2 3h5l3 13h15l3-10H9" fill="none" stroke="#3fbf98" stroke-width="2.5"/><circle cx="12" cy="21" r="2.5"/><circle cx="23" cy="21" r="2.5"/></svg>Personal Shopper</li>
    <li><svg viewBox="0 0 30 26" aria-hidden="true"><path d="M6 8h18l2 16H4z"/><path d="M10 9V5a5 5 0 0 1 10 0v4" fill="none" stroke="#3fbf98" stroke-width="2"/></svg>Running Errands</li>
    <li><svg viewBox="0 0 30 26" aria-hidden="true"><path d="M15 1l13 11h-4v12H6V12H2z"/><rect x="12" y="15" width="6" height="9" fill="#0b0b0b"/></svg>Property Management</li>
    <li><svg viewBox="0 0 30 26" role="img" aria-label="event planning icon"><rect x="4" y="3" width="22" height="20" rx="5"/></svg>Event Planning</li>
  </ul>
</section>

<section class="card card--contact" aria-label="Front of card: contact">
  <svg class="backdrop" viewBox="0 0 560 320" width="560" height="320" aria-hidden="true">
    <path d="M0 292 C170 300 390 230 560 100 L560 320 L0 320 Z" fill="#0b0b0b"/>
    <path d="M300 205 C400 170 490 110 560 30 L560 60 C480 135 400 185 300 205 Z" fill="#3fbf98"/>
  </svg>
  <div class="brand">Harbor Concierge</div>
  <div class="portrait" role="img" aria-label="Portrait photo of Tamsin Heller"></div>
  <div class="contact">
    <div class="contact__name">Tamsin Heller</div>
    <div class="contact__line"><svg viewBox="0 0 14 14" aria-hidden="true"><path d="M3 1l2 3-1.5 1.5a8 8 0 0 0 5 5L10 9l3 2-1 2.5C6 14 0 8 .5 2z"/></svg>305-482-9167</div>
    <div class="contact__line"><svg viewBox="0 0 14 14" aria-hidden="true"><path d="M1 3h12v9H1z"/><path d="M1 3l6 5 6-5" fill="none" stroke="#0b0b0b" stroke-width="1.2"/></svg>quaylineerrands@mailvora.net</div>
  </div>
</section>

</body>
</html>
```